Logo for Law Office
K. Morland Law
Creative Brief
Professional
Luis T. Fenwick
Attorney at Law
4870 Dunmore St. Suite C-07 Corpus Christi, TX 78401
luisfenwick7@mailvista.com

```html
<!DOCTYPE html>
<html lang="en">
<head>
<meta charset="utf-8">
<title>K. Morland Law — Business Card</title>
<link rel="stylesheet" href="https://fonts.googleapis.com/css2?family=Montserrat:wght@400;500;600&display=swap">
<style>
  :root {
    --backdrop: #8e8e8e;
    --card: #0d0d0d;
    --card-edge: #1c1c1c;
    --gold: #d4a53c;
    --gold-deep: #a97a1f;
    --ink-soft: #c9a24a;
  }
  * { box-sizing: border-box; margin: 0; padding: 0; }
  html, body { width: 1200px; height: 908px; overflow: hidden; }
  body {
    background: var(--backdrop);
    font-family: "Montserrat", Arial, sans-serif;
    position: relative;
  }
  .card {
    position: absolute;
    top: 299px;
    width: 520px;
    height: 310px;
    border-radius: 22px;
    background: linear-gradient(150deg, var(--card-edge) 0%, var(--card) 45%, var(--card) 100%);
    overflow: hidden;
    box-shadow: 0 14px 30px rgba(0,0,0,0.35);
  }
  .card--front { left: 60px; }
  .card--back { left: 620px; }

  .brand {
    position: absolute;
    display: flex;
    flex-direction: column;
    align-items: center;
  }
  .brand__mark {
    width: 14px; height: 14px;
    border-radius: 50%;
    background: var(--gold);
    margin-bottom: 14px;
  }
  .brand__name {
    color: var(--gold);
    font-weight: 600;
    letter-spacing: 0.08em;
    text-transform: uppercase;
    white-space: nowrap;
  }
  .brand__rule {
    height: 1px;
    background: var(--gold);
    margin-top: 8px;
  }
  .card--front .brand { left: 0; right: 0; top: 120px; }
  .card--front .brand__name { font-size: 26px; }
  .card--front .brand__rule { width: 200px; }

  .card--back .brand { left: 30px; width: 210px; top: 165px; }
  .card--back .brand__name { font-size: 19px; }
  .card--back .brand__rule { width: 150px; }

  .contact {
    position: absolute;
    left: 260px;
    top: 42px;
    color: var(--ink-soft);
    font-size: 11px;
    line-height: 1.55;
  }
  .contact__name { font-size: 16px; font-weight: 600; color: var(--gold); }
  .contact__role { font-size: 12px; font-weight: 500; margin-bottom: 16px; }
  .contact__row { display: flex; align-items: center; gap: 7px; }
  .contact__row svg { width: 11px; height: 11px; flex: none; }
  .contact__address { margin-bottom: 10px; }

  .gold-band {
    position: absolute;
    right: 0; top: 0; bottom: 0;
    width: 30px;
    background: linear-gradient(90deg, var(--gold-deep), var(--gold) 55%, var(--gold-deep));
  }
  .gold-band__notch {
    position: absolute;
    right: 0; top: 150px;
    width: 30px; height: 4px;
    background: var(--card);
  }
</style>
</head>
<body>
  <section class="card card--front" aria-label="Card front">
    <div class="brand">
      <span class="brand__mark"></span>
      <span class="brand__name">K. Morland Law</span>
      <span class="brand__rule"></span>
    </div>
  </section>

  <section class="card card--back" aria-label="Card back">
    <div class="brand">
      <span class="brand__mark"></span>
      <span class="brand__name">K. Morland Law</span>
      <span class="brand__rule"></span>
    </div>

    <div class="contact">
      <p class="contact__name">Luis T. Fenwick</p>
      <p class="contact__role">Attorney at Law</p>
      <p class="contact__address">4870 Dunmore St. Suite C-07<br>Corpus Christi, TX 78401</p>
      <p class="contact__row">
        <svg viewBox="0 0 12 12" aria-hidden="true"><circle cx="6" cy="6" r="5.5" fill="none" stroke="#d4a53c"/><path d="M4 3.2l1 1.4-.6.7c.4.9 1 1.5 1.9 1.9l.7-.6 1.4 1-.6 1.2C5.6 8.6 3.4 6.4 3 4.2z" fill="#d4a53c"/></svg>
        361 555 0142
      </p>
      <p class="contact__row">
        <svg viewBox="0 0 12 12" aria-hidden="true"><circle cx="6" cy="6" r="5.5" fill="none" stroke="#d4a53c"/><path d="M4 3.2l1 1.4-.6.7c.4.9 1 1.5 1.9 1.9l.7-.6 1.4 1-.6 1.2C5.6 8.6 3.4 6.4 3 4.2z" fill="#d4a53c"/></svg>
        361 555 0187
      </p>
      <p class="contact__row">
        <svg viewBox="0 0 12 12" aria-hidden="true"><circle cx="6" cy="6" r="5.5" fill="none" stroke="#d4a53c"/><rect x="3" y="4" width="6" height="4" fill="none" stroke="#d4a53c" stroke-width="0.8"/><path d="M3 4l3 2.2L9 4" fill="none" stroke="#d4a53c" stroke-width="0.8"/></svg>
        luisfenwick7@mailvista.com
      </p>
    </div>

    <div class="gold-band"><span class="gold-band__notch"></span></div>
  </section>
</body>
</html>
```